Poster Design Project

Poster with modern feeling to be displayed in office. The text that needs to be included in this poster is below:

Rules
1. If it’s not in writing it doesn’t exist.
2. No such thing as 'off the record.'
3. Do not hold a private conversation in a public place.
4. Don’t believe any number that ends in zero.
5. Never turn down an opportunity to eat or go to the bathroom.
6. Don’t spend any of your own money. Don’t even admit you own a credit card. Don’t spend money that is not yours.
7. Not always a 'right' or 'wrong' answer - 'It depends.'
8. In a campaign, someone has to be in charge – campaigns are a place to foster democracy, not practice it.
9. Assume nothing.
10. If you make a mistake, fix it before analyzing. Bad news doesn’t age well.

Industry/Entity Type

Credit Card

Requirements
Must have
• Rules
7. Not always a “right” or “wrong” answer - 'It depends.' 
9. Assume nothing.

```html
<!DOCTYPE html>
<html lang="en">
<head>
<meta charset="utf-8">
<title>Rules</title>
<link rel="stylesheet" href="https://fonts.googleapis.com/css2?family=Oswald:wght@500;600;700&family=Rubik+Wet+Paint&family=Rokkitt:wght@500;700&display=swap">
<style>
  :root {
    --ink-dark: #0d120f;
    --plate-mid: #1c2a22;
    --plate-glow: #4d6f5b;
    --cream: #e9d996;
    --salmon: #f3a77a;
    --amber: #eba238;
  }
  html, body {
    margin: 0;
    width: 848px;
    height: 1200px;
    overflow: hidden;
    background: var(--ink-dark);
  }
  .poster {
    position: relative;
    width: 848px;
    height: 1200px;
  }
  .poster__texture {
    position: absolute;
    inset: 0;
    background:
      radial-gradient(ellipse 45% 22% at 32% 37%, rgba(77,111,91,.85), transparent 70%),
      radial-gradient(ellipse 40% 25% at 62% 70%, rgba(77,111,91,.55), transparent 75%),
      radial-gradient(ellipse 70% 60% at 50% 50%, var(--plate-mid), var(--ink-dark) 85%);
  }
  .poster__type {
    position: absolute;
    inset: 0;
    width: 848px;
    height: 1200px;
  }
  .cond { font-family: "Oswald", "Arial Narrow", sans-serif; font-weight: 600; }
  .drip { font-family: "Rubik Wet Paint", "Impact", sans-serif; }
  .serif { font-family: "Rokkitt", "Georgia", serif; font-weight: 700; }
  .cream { fill: var(--cream); }
  .salmon { fill: var(--salmon); }
  .amber { fill: var(--amber); }
</style>
</head>
<body>
<main class="poster">
  <div class="poster__texture" role="img" aria-label="Dark green diamond-plate metal texture with a soft glow"></div>
  <svg class="poster__type" viewBox="0 0 800 1132" xmlns="http://www.w3.org/2000/svg">
    <g class="rules-list">
      <text class="title cond cream" x="305" y="92" font-size="78" textLength="185" lengthAdjust="spacingAndGlyphs">RULES</text>

      <text class="rule cond cream" x="38" y="165" font-size="54" textLength="717" lengthAdjust="spacingAndGlyphs">IF IT’S NOT IN WRITING IT DOESN’T EXIST</text>
      <text class="rule serif salmon" x="38" y="232" font-size="58" textLength="717" lengthAdjust="spacing">NO SUCH THING AS</text>
      <text class="rule drip salmon" x="36" y="300" font-size="74" textLength="722" lengthAdjust="spacingAndGlyphs">OFF THE RECORD</text>
      <text class="rule cond cream" x="36" y="355" font-size="32" textLength="716" lengthAdjust="spacingAndGlyphs">DO NOT HOLD A PRIVATE CONVERSATION IN A PUBLIC PLACE</text>
      <text class="rule cond cream" x="36" y="400" font-size="50" textLength="716" lengthAdjust="spacingAndGlyphs">DONT BELIEVE ANY NUMBER THAT ENDS IN</text>
      <text class="rule drip cream" x="38" y="500" font-size="112" textLength="382" lengthAdjust="spacingAndGlyphs">ZERO</text>

      <text class="rule cond amber" x="445" y="452" font-size="38" textLength="307" lengthAdjust="spacingAndGlyphs">NEVER TURN DOWN</text>
      <text class="rule cond amber" x="445" y="505" font-size="34" textLength="307" lengthAdjust="spacingAndGlyphs">AN OPPORTUNITY TO EAT</text>
      <text class="rule cond cream" x="357" y="560" font-size="38" textLength="395" lengthAdjust="spacingAndGlyphs">OR GO TO THE BATHROOM</text>

      <text class="rule cond cream" x="38" y="620" font-size="60" textLength="720" lengthAdjust="spacingAndGlyphs">DONT SPEND ANY OF YOUR OWN MONEY</text>
      <text class="rule cond salmon" x="38" y="675" font-size="50" textLength="720" lengthAdjust="spacingAndGlyphs">DONT EVEN ADMIT YOU OWN A CREDIT CARD</text>

      <text class="rule cond cream" x="38" y="755" font-size="72" textLength="347" lengthAdjust="spacingAndGlyphs">DONT SPEND</text>
      <text class="rule cond cream" x="38" y="835" font-size="72" textLength="347" lengthAdjust="spacingAndGlyphs">MONEY THAT</text>
      <text class="rule cond cream" x="38" y="917" font-size="72" textLength="347" lengthAdjust="spacingAndGlyphs">IS NOT YOURS</text>

      <text class="rule serif salmon" transform="translate(400 698) rotate(90)" font-size="28" textLength="250" lengthAdjust="spacingAndGlyphs">NOT ALWAYS A</text>
      <text class="rule drip cream" transform="translate(444 700) rotate(90)" font-size="38" textLength="248" lengthAdjust="spacingAndGlyphs">WRONG</text>
      <text class="rule drip cream" transform="translate(478 700) rotate(90)" font-size="38" textLength="250" lengthAdjust="spacingAndGlyphs">ANSWER</text>
      <text class="rule drip amber" transform="translate(590 700) rotate(90)" font-size="40" textLength="245" lengthAdjust="spacingAndGlyphs">IT DEPENDS</text>
      <text class="rule cond amber" transform="translate(640 745) rotate(90)" font-size="86" font-weight="700" textLength="195" lengthAdjust="spacingAndGlyphs">RIGHT</text>
      <text class="rule serif amber" transform="translate(700 698) rotate(90)" font-size="28" textLength="42" lengthAdjust="spacingAndGlyphs">OR</text>

      <text class="rule cond cream" x="38" y="980" font-size="42" textLength="720" lengthAdjust="spacingAndGlyphs">IN A CAMPAIGN SOMEONE HAS TO BE IN CHARGE</text>
      <text class="rule cond amber" x="38" y="1018" font-size="26" textLength="720" lengthAdjust="spacingAndGlyphs">CAMPAIGNS ARE A PLACE TO FOSTER DEMOCRACY, NOT PRACTICE IT</text>
      <text class="rule cond cream" x="38" y="1100" font-size="74" textLength="394" lengthAdjust="spacingAndGlyphs">ASSUME NOTHING</text>

      <text class="rule serif salmon" x="437" y="1055" font-size="24" textLength="321" lengthAdjust="spacing">IF YOU MAKE A MISTAKE, FIX IT</text>
      <text class="rule serif salmon" x="437" y="1083" font-size="24" textLength="321" lengthAdjust="spacing">BEFORE ANALYZING. BAD NEWS</text>
      <text class="rule serif salmon" x="437" y="1108" font-size="22" textLength="156" lengthAdjust="spacingAndGlyphs">DOESN’T AGE WELL</text>
    </g>
  </svg>
</main>
</body>
</html>
```